Helping Seniors and their families start the discussion about driver safety, and explore options to preserve senior independence.
Target Market(s)
Seniors and their families
Industry/Entity Type
Non Profit
Number of Pages Required
4 page
Font styles to use
Sans Serif
Requirements
Must have
- Logo
- Application for Amber Crossings Registration

Nice to have
- Colorful, and designed for Senior Citizens and their Families

```html
<!DOCTYPE html>
<html lang="en">
<head>
<meta charset="utf-8">
<title>Amber Crossings</title>
<link href="https://fonts.googleapis.com/css2?family=Open+Sans:wght@400;600;700;800&display=swap" rel="stylesheet">
<style>
:root{
  --green:#1f9d4c;
  --green-dark:#13823b;
  --ink:#2b2b2b;
  --muted:#7a7a7a;
  --light:#f3f3f3;
  --line:#e2e2e2;
  --footer-bar:#2a2a2a;
}
*{box-sizing:border-box;margin:0;padding:0}
html,body{width:1200px;height:3556px;overflow:hidden}
body{font-family:"Open Sans",Arial,sans-serif;color:var(--ink);background:#fff}
section,header,footer{position:relative;width:1200px;overflow:hidden}
.btn{display:inline-block;background:var(--green);color:#fff;font-size:12px;font-weight:700;text-transform:uppercase;padding:9px 18px;border-radius:3px}
.section-title{text-align:center;font-size:26px;font-weight:700;text-transform:uppercase;letter-spacing:.5px}
.section-title::after{content:"";display:block;width:60px;height:3px;background:var(--green);margin:12px auto 0}

/* header */
.site-header{height:108px;border-bottom:1px solid var(--line)}
.brand{position:absolute;left:36px;top:22px;display:flex;align-items:center;gap:12px}
.brand-dot{width:40px;height:40px;border-radius:50%;background:var(--green)}
.brand-name{font-size:30px;font-weight:700;color:var(--green);line-height:1}
.top-contact{position:absolute;right:40px;top:14px;font-size:12px;color:var(--muted);display:flex;gap:28px}
.main-nav{position:absolute;right:40px;top:62px;display:flex;gap:34px;font-size:14px;font-weight:600;text-transform:uppercase}
.main-nav .active{color:var(--green);border-bottom:2px solid var(--green);padding-bottom:8px}

/* hero */
.hero{height:546px;background:linear-gradient(120deg,#5d6b76 0%,#8e8a80 35%,#6f6a5e 60%,#9aa6ab 100%)}
.hero-inner{position:absolute;top:360px;left:0;width:100%;text-align:center;color:#fff}
.hero h1{font-size:46px;font-weight:800;letter-spacing:1px}
.hero p{font-size:14px;line-height:1.5;margin:8px auto 16px;width:560px}

/* why */
.why{height:428px}
.why .section-title{padding-top:78px}
.why-intro{width:760px;margin:22px auto 0;text-align:center;font-size:13px;line-height:1.6;color:var(--muted)}
.features{display:flex;justify-content:center;gap:78px;margin-top:54px}
.feature{text-align:center;width:170px}
.feature-icon{width:92px;height:92px;border-radius:50%;border:3px solid #cfe9d7;margin:0 auto;display:flex;align-items:center;justify-content:center}
.feature-icon span{width:74px;height:74px;border-radius:50%;background:var(--green);display:flex;align-items:center;justify-content:center}
.feature h3{font-size:15px;font-weight:700;margin-top:16px;white-space:nowrap}
.slider-arrow{position:absolute;top:224px;font-size:34px;color:#c8c8c8}

/* reservation */
.reservation{height:506px;background:var(--light)}
.reservation .section-title{padding-top:74px}
.steps{position:absolute;left:0;top:0;width:1200px;height:506px}
.step-box{position:absolute;width:160px;height:78px;background:#fff;border:2px solid var(--green);font-size:11px;line-height:1.5;text-align:center;padding:10px 12px;color:var(--muted);display:flex;align-items:center;justify-content:center}
.step-num{position:absolute;width:32px;height:32px;border-radius:50%;background:var(--green);color:#fff;font-weight:700;font-size:15px;display:flex;align-items:center;justify-content:center}
.res-line{position:absolute;top:356px;width:100%;text-align:center}
.res-line h4{color:var(--green);font-size:18px;font-weight:700;text-transform:uppercase}
.res-line p{font-size:26px;font-weight:800;margin-top:2px}

/* service band */
.service-band{height:372px;background:linear-gradient(135deg,#7c8c97,#c9c6bc 55%,#9da7ab)}
.service-green{position:absolute;inset:0;background:var(--green);clip-path:polygon(0 0,840px 0,760px 100%,0 100%)}
.service-band h2{position:absolute;left:40px;top:40px;color:#fff;font-size:20px;font-weight:700;text-transform:uppercase}
.service-list{position:absolute;top:104px;list-style:none;color:#fff;font-size:13px}
.service-list li{margin-bottom:15px;display:flex;align-items:center;gap:10px}
.service-list li::before{content:"";width:6px;height:6px;border-radius:50%;background:#fff}

/* blog */
.blog{height:692px}
.blog .section-title{padding-top:150px}
.posts{display:flex;justify-content:center;gap:36px;margin-top:50px}
.post{width:290px}
.post-img{height:230px}
.post h3{font-size:13px;font-weight:700;text-transform:uppercase;margin-top:16px}
.post p{font-size:11px;line-height:1.5;color:var(--muted);margin:6px 0 12px}

/* testimonials */
.testimonials{height:534px}
.testimonials .section-title{padding-top:10px}
.quote-panel{position:absolute;left:70px;top:84px;width:880px;height:340px;background:#ecebe8;padding:46px 60px 0 110px}
.quote-mark{position:absolute;font-size:80px;font-weight:800;color:var(--green);line-height:1}
.quote-panel p{font-size:14px;line-height:1.7;color:#555}
.quote-author{text-align:right;margin-top:22px;font-weight:700;font-size:14px}
.quote-author small{display:block;font-weight:400;color:var(--muted);font-size:12px}
.quote-photo{position:absolute;right:60px;top:110px;width:210px;height:400px}
.dots{position:absolute;top:484px;width:100%;text-align:center}
.dots span{display:inline-block;width:9px;height:9px;border-radius:50%;background:#c8c8c8;margin:0 3px}
.dots span.on{background:var(--green)}

/* footer */
.site-footer{height:330px;background:var(--light)}
.footer-cols{display:flex;padding:40px 70px 0;gap:60px}
.footer-col h5{font-size:14px;font-weight:700;text-transform:uppercase;margin-bottom:16px}
.footer-col li{list-style:none;font-size:12px;color:#555;margin-bottom:10px}
.footer-col.links li::before{content:"\203A";color:var(--green);margin-right:8px}
.social{display:flex;gap:8px;margin-top:12px}
.social span{width:24px;height:24px;border-radius:50%;border:1px solid #999}
.field{width:200px;height:30px;border:1px solid #ccc;background:#fff;font-size:11px;color:#999;padding:7px 10px;margin-bottom:8px}
.partner-badge{width:110px;height:40px;background:#d9d9d9;border-radius:4px}
.footer-bar{position:absolute;bottom:0;left:0;width:100%;height:36px;background:var(--footer-bar);color:#bbb;font-size:11px;text-align:center;line-height:36px}
</style>
</head>
<body>

<header class="site-header">
  <div class="brand"><span class="brand-dot"></span><span class="brand-name">Amber Crossings</span></div>
  <div class="top-contact"><span>&#9742; 555-014-2290</span><span>&#9993; hello@ambercrossings.org</span></div>
  <nav class="main-nav">
    <span class="active">Home</span><span>About Us</span><span>Requirements</span><span>Why Us</span><span>Blog</span><span>Contact</span>
  </nav>
</header>

<section class="hero" role="img" aria-label="Photo of a senior man and a younger companion standing beside a car">
  <div class="hero-inner">
    <h1>AMBER CROSSINGS</h1>
    <p>Safe, friendly rides that keep seniors connected to the places and people that matter most to them every day.</p>
    <span class="btn">Read More</span>
  </div>
</section>

<section class="why">
  <h2 class="section-title">Why Amber Crossings</h2>
  <p class="why-intro">We help seniors and their families talk openly about driving safety and find dependable ways to get around. Our trained drivers treat every rider with patience and respect, so independence never has to end.</p>
  <span class="slider-arrow" style="left:150px">&#8249;</span>
  <span class="slider-arrow" style="right:150px">&#8250;</span>
  <div class="features">
    <div class="feature"><div class="feature-icon"><span><svg width="34" height="34" viewBox="0 0 34 34"><rect x="4" y="6" width="26" height="24" rx="2" fill="none" stroke="#fff" stroke-width="3"/><line x1="4" y1="13" x2="30" y2="13" stroke="#fff" stroke-width="3"/></svg></span></div><h3>Convenience</h3></div>
    <div class="feature"><div class="feature-icon"><span><svg width="34" height="34" viewBox="0 0 34 34"><circle cx="17" cy="17" r="12" fill="none" stroke="#fff" stroke-width="3"/><circle cx="17" cy="17" r="4" fill="#fff"/></svg></span></div><h3>Specialized services</h3></div>
    <div class="feature"><div class="feature-icon"><span><svg width="34" height="34" viewBox="0 0 34 34"><path d="M17 4 L28 9 V17 C28 24 23 29 17 31 C11 29 6 24 6 17 V9 Z" fill="none" stroke="#fff" stroke-width="3"/><path d="M11 17 L15 21 L23 13" fill="none" stroke="#fff" stroke-width="3"/></svg></span></div><h3>Safety</h3></div>
    <div class="feature"><div class="feature-icon"><span><svg width="34" height="34" viewBox="0 0 34 34"><circle cx="17" cy="17" r="12" fill="none" stroke="#fff" stroke-width="3"/><text x="17" y="23" text-anchor="middle" font-size="16" font-weight="700" fill="#fff" font-family="Open Sans, sans-serif">$</text></svg></span></div><h3>Affordable Rates</h3></div>
  </div>
</section>

<section class="reservation">
  <h2 class="section-title">Reservation Process</h2>
  <div class="steps">
    <svg width="1200" height="506" style="position:absolute;left:0;top:0">
      <path d="M430 283 H520" stroke="#1f9d4c" stroke-width="2" fill="none"/>
      <path d="M512 277 L520 283 L512 289" stroke="#1f9d4c" stroke-width="2" fill="none"/>
      <path d="M680 263 H760" stroke="#1f9d4c" stroke-width="2" fill="none"/>
      <path d="M752 257 L760 263 L752 269" stroke="#1f9d4c" stroke-width="2" fill="none"/>
    </svg>
    <div class="step-box" style="left:270px;top:244px">We ask for 24 hours' notice for each reservation.</div>
    <div class="step-num" style="left:334px;top:330px">1</div>
    <div class="step-num" style="left:584px;top:182px">2</div>
    <div class="step-box" style="left:520px;top:224px">Reservations can be made 7 days a week between 8 am and 5 pm.</div>
    <div class="step-box" style="left:760px;top:224px">Leave your name and phone number if no one answers.</div>
    <div class="step-num" style="left:824px;top:310px">3</div>
    <div class="res-line"><h4>Reservation Line</h4><p>555-014-2290</p></div>
  </div>
</section>

<section class="service-band" role="img" aria-label="Photo of a driver helping a senior in a wheelchair into a van">
  <div class="service-green"></div>
  <h2>Go when and where you want to go with Amber Crossings</h2>
  <ul class="service-list" style="left:40px">
    <li>Medical Appointments</li><li>Dental Appointments</li><li>Outpatient Testing and Procedures</li><li>Physical Therapy</li><li>Dialysis Clinic</li><li>Radiation Clinic</li><li>Church Events</li>
  </ul>
  <ul class="service-list" style="left:380px">
    <li>Senior Centers/Adult Day Care Centers</li><li>Hospital/Nursing Home Discharge</li><li>Airport Transportation</li><li>Special Family Events</li><li>Grocery Shopping and Other Types of Shopping</li><li>Bank and Post Office Errands</li><li>Senior/Beauty Shop Appointments</li>
  </ul>
</section>

<section class="blog">
  <h2 class="section-title">Our Blog</h2>
  <div class="posts">
    <article class="post"><div class="post-img" role="img" aria-label="Photo of a senior being helped into a car" style="background:linear-gradient(135deg,#8a6d5a,#c7b6a4)"></div><h3>Starting the driving talk</h3><p>Simple tips for starting a kind conversation with a parent about when to stop driving.</p><span class="btn">Read More</span></article>
    <article class="post"><div class="post-img" role="img" aria-label="Photo of a senior couple walking with a caregiver" style="background:linear-gradient(135deg,#6f7a6a,#b9b3a6)"></div><h3>Planning rides together</h3><p>How families can plan rides together and keep loved ones active in their community.</p><span class="btn">Read More</span></article>
    <article class="post"><div class="post-img" role="img" aria-label="Photo of a senior in a wheelchair beside a van" style="background:linear-gradient(135deg,#8fa3b4,#d6d8d6)"></div><h3>Your first ride with us</h3><p>What to expect on your first ride and how our drivers help with mobility needs.</p><span class="btn">Read More</span></article>
  </div>
</section>

<section class="testimonials">
  <h2 class="section-title">Testimonials</h2>
  <div class="quote-panel">
    <span class="quote-mark" style="left:40px;top:30px">&ldquo;</span>
    <p>Thank you for helping my mother keep her weekly routine. The drivers are always on time, patient and kind, and she looks forward to every trip. Our whole family feels calmer knowing she is safe on the road and still free to visit friends, attend church and run her own errands whenever she likes.</p>
    <span class="quote-mark" style="right:40px;top:220px">&rdquo;</span>
    <div class="quote-author">Marion Hale<small>Happy Rider</small></div>
  </div>
  <div class="quote-photo" role="img" aria-label="Photo of a smiling senior woman" style="background:linear-gradient(180deg,#d8d2c8,#a9a29a)"></div>
  <div class="dots"><span></span><span class="on"></span><span></span><span></span></div>
</section>

<footer class="site-footer">
  <div class="footer-cols">
    <div class="footer-col" style="width:260px">
      <h5>Contact Us</h5>
      <ul>
        <li>&#9873; 120 Maple Grove Road, Suite 4, Springfield</li>
        <li>&#9742; Call Us: 555-014-2290</li>
        <li>&#9993; Mail: hello@ambercrossings.org</li>
      </ul>
      <div class="social"><span></span><span></span><span></span><span></span></div>
    </div>
    <div class="footer-col links" style="width:170px">
      <h5>Quick Links</h5>
      <ul><li>Home</li><li>Who us</li><li>About us</li><li>Requirements</li><li>Contact</li></ul>
    </div>
    <div class="footer-col links" style="width:190px">
      <h5>Other Links</h5>
      <ul><li>Disclaimer</li><li>Terms &amp; Conditions</li><li>Privacy Policy</li><li>Policy</li><li>Sitemap</li></ul>
    </div>
    <div class="footer-col">
      <h5>Contact Form</h5>
      <div class="field">Enter Name</div>
      <div class="field">Enter Email</div>
      <div style="display:flex;align-items:center;gap:30px"><span class="btn">Submit</span><span class="partner-badge"></span></div>
    </div>
  </div>
  <div class="footer-bar">Copyright 2017 Amber Crossings All Rights Reserved</div>
</footer>

</body>
</html>
```